ORVAN LOGIC LTD

See website just wanted it updated and more fresh ; https://www.orvan-logic.co.uk

Coding

Coded - Design and coding required

Colors

Designer to choose colors to be used in the design.

```html
<!DOCTYPE html>
<html lang="en">
<head>
<meta charset="utf-8">
<title>Orvan Logic – Education Support and Installation</title>
<link href="https://fonts.googleapis.com/css2?family=Open+Sans:ital,wght@0,400;0,600;0,700;1,400&family=Marcellus&display=swap" rel="stylesheet">
<style>
:root{
  --blue:#1f72c4;
  --blue-dark:#145ca6;
  --orange:#f05a28;
  --ink:#222;
  --text:#444;
  --muted:#666;
  --line:#b9d3ec;
  --dark-panel:#2a2a2a;
  --white:#fff;
  --chat:#5cbf5a;
}
*{margin:0;padding:0;box-sizing:border-box}
html,body{width:1200px;height:4655px;overflow:hidden;background:var(--white)}
body{position:relative;font-family:"Open Sans",Arial,sans-serif;color:var(--text)}
.abs{position:absolute}
.brand{display:flex;align-items:center;gap:10px;font-family:"Open Sans",Arial,sans-serif;font-weight:700;font-size:30px;color:var(--blue)}
.brand-square{width:22px;height:22px;background:var(--orange)}
.btn{position:absolute;display:flex;align-items:center;justify-content:center;background:var(--orange);color:var(--white);border-radius:24px;font-size:16px;text-transform:uppercase;letter-spacing:.3px}
/* header */
.header{top:0;left:0;width:1200px;height:90px}
.contact-pill{position:absolute;display:flex;align-items:center;gap:16px;font-size:20px;color:var(--ink)}
.contact-pill .ico{width:50px;height:50px;border-radius:50%;background:var(--blue);display:flex;align-items:center;justify-content:center}
.nav{top:90px;left:0;width:1200px;height:60px;background:var(--blue);display:flex;justify-content:center;align-items:center;gap:57px;padding-right:20px}
.nav a{color:var(--white);text-decoration:none;font-size:19px}
.nav a.active{color:#f6a07a}
/* hero */
.hero{top:150px;left:0;width:1200px;height:558px;background:linear-gradient(120deg,#6e7f8a 0%,#b49a7a 40%,#8a6a4c 70%,#caa986 100%)}
.hero-band{top:412px;left:0;width:611px;height:157px;background:rgba(31,114,196,.75)}
.hero-title{top:425px;left:121px;font-family:"Marcellus",serif;font-size:68px;color:var(--white);letter-spacing:2px}
.hero-sub{top:518px;left:122px;font-family:"Marcellus",serif;font-size:22px;color:var(--white);letter-spacing:1px}
.dot{position:absolute;width:12px;height:12px;border-radius:50%;background:var(--white)}
/* about */
.h2{position:absolute;font-weight:700;color:var(--ink);letter-spacing:1px}
.about-text{top:904px;left:118px;width:547px;font-size:16px;line-height:34px;text-align:justify;color:var(--text)}
/* support */
.support-img{top:1343px;left:0;width:522px;height:359px;background:linear-gradient(135deg,#4b5a68,#9a7a64 50%,#3c4b5a)}
.support-panel{top:1393px;left:455px;width:633px;height:362px;background:var(--dark-panel);color:var(--white);padding:40px 32px 0 48px}
.support-panel h3{font-weight:400;font-size:28px;line-height:47px;letter-spacing:1px}
.support-panel p{margin-top:14px;font-size:16px;line-height:34.5px;color:#e8e8e8}
/* services */
.center{left:0;width:1200px;text-align:center}
.card{position:absolute;top:2089px;width:284px;height:316px;border:2px solid var(--line);background:var(--white);text-align:center}
.card-icon{position:absolute;top:-56px;left:79px;width:126px;height:126px;border-radius:50%;background:#eaf3fb;border:3px solid var(--line);border-bottom:6px solid var(--blue)}
.card h4{position:absolute;top:92px;left:0;width:100%;font-weight:600;font-size:23px;line-height:32px;color:var(--ink)}
.card p{position:absolute;top:156px;left:14px;right:14px;font-size:15px;line-height:30px;color:var(--muted)}
/* testimonials */
.testi{top:2526px;left:0;width:1200px;height:432px;background:linear-gradient(180deg,#1c6fc0,#2280d2)}
.testi-quote{top:2694px;left:160px;width:880px;text-align:center;font-size:17px;line-height:37px;color:var(--white)}
.testi-author{top:2833px;font-style:italic;font-size:16px;color:var(--white)}
.quote-mark{position:absolute;font-family:Georgia,serif;font-size:90px;color:var(--white);line-height:1}
/* partners */
.partner{position:absolute;top:3182px;width:187px;height:81px;border:2px solid #d4d4d4;background:var(--white);display:flex;align-items:center;justify-content:center}
.partner span{display:block;width:80px;height:22px;border-radius:4px;background:#c9ced4}
/* stats */
.stats{top:3368px;left:0;width:1200px;height:338px;background:linear-gradient(180deg,#1a5ea8,#2a7fd0)}
.stat{position:absolute;top:3453px;width:170px;height:170px;border-radius:50%;background:var(--white);text-align:center;padding-top:42px}
.stat b{display:block;font-size:33px;color:var(--blue);font-weight:700}
.stat i{display:block;font-style:normal;font-size:26px;color:#333;margin-top:4px}
/* contact */
.info{position:absolute;left:195px;font-size:20px;line-height:33px;color:#333}
.field{position:absolute;border:1px solid #cfcfcf;background:var(--white);font-size:15px;color:#555;padding:14px 16px}
.live-chat{top:4254px;left:1021px;width:170px;height:50px;background:var(--chat);border-radius:4px;display:flex;align-items:center;justify-content:center;gap:12px;color:var(--white);font-weight:700;font-size:18px}
/* footer */
.footer{top:4344px;left:0;width:1200px;height:311px;background:var(--blue)}
.foot-brand{top:4392px;left:500px;width:200px;height:48px;background:var(--white);justify-content:center;font-size:26px}
.foot-nav{top:4478px;display:flex;justify-content:center;gap:56px;font-size:19px;color:var(--white)}
.social{position:absolute;top:4536px;width:36px;height:36px;border-radius:50%;border:2px solid var(--white)}
.copyright{top:4606px;font-size:16px;color:var(--white)}
</style>
</head>
<body>

<!-- Header -->
<div class="abs header">
  <div class="abs brand" style="top:18px;left:112px"><span class="brand-square"></span>Orvan Logic</div>
  <div class="contact-pill" style="top:16px;left:600px">
    <span class="ico"><svg width="22" height="16" viewBox="0 0 22 16"><rect x="1" y="1" width="20" height="14" rx="2" fill="none" stroke="#fff" stroke-width="2"/><path d="M1 2l10 7 10-7" fill="none" stroke="#fff" stroke-width="2"/></svg></span>
    info@orvan-logic.co.uk
  </div>
  <div class="contact-pill" style="top:16px;left:874px">
    <span class="ico"><svg width="22" height="22" viewBox="0 0 24 24"><path d="M6.6 10.8a15 15 0 006.6 6.6l2.2-2.2a1 1 0 011-.25 11.4 11.4 0 003.6.57 1 1 0 011 1V20a1 1 0 01-1 1A17 17 0 013 4a1 1 0 011-1h3.5a1 1 0 011 1 11.4 11.4 0 00.57 3.6 1 1 0 01-.25 1z" fill="#fff"/></svg></span>
    <span style="font-weight:600">0161 555 0192</span>
  </div>
</div>
<nav class="abs nav">
  <a class="active">HOME</a><a>SERVICES</a><a>ABOUT US</a><a>HELPDESK</a><a>CONTACT US</a>
</nav>

<!-- Hero -->
<div class="abs hero" role="img" aria-label="Photo of a person working on a laptop at a wooden desk with a coffee cup"></div>
<div class="abs hero-band"></div>
<div class="abs hero-title">ORVAN LOGIC</div>
<div class="abs hero-sub">EDUCTION SUPPORT AND INSTALLATION</div>
<span class="dot" style="top:402px;left:1074px;background:var(--blue)"></span>
<span class="dot" style="top:428px;left:1074px"></span>
<span class="dot" style="top:450px;left:1074px"></span>

<!-- About -->
<h2 class="h2" style="top:828px;left:117px;font-size:33px">ABOUT US</h2>
<div class="abs about-text">
  Orvan Logic, is a registered UK Limited Company<br>
  Our goal is to provide comprehensive ICT support along with excellent customer service to the education sector.<br>
  Lorem ipsum dolor sit amet, consectetur adipiscing elit, sed do eiusmod tempor incididunt ut labore et dolore magna aliqua. Quis ipsum suspendisse ultrices gravida. Risus commodo viverra maecenas accumsan lacus vel facilisis. Lorem ipsum dolor sit amet, consectetur adipiscing elit.
</div>
<div class="btn" style="top:1202px;left:108px;width:154px;height:45px">Read more</div>
<div class="abs" style="top:841px;left:752px;width:338px;height:338px;border-radius:50%;background:var(--blue)"></div>
<div class="abs" role="img" aria-label="Photo of a woman working at a computer in a bright office" style="top:846px;left:766px;width:322px;height:322px;border-radius:50%;background:linear-gradient(135deg,#f3f3f3,#d9d4cf 60%,#b8aca2);border:4px solid #fff"></div>

<!-- Support -->
<div class="abs support-img" role="img" aria-label="Photo of two technicians reviewing a laptop in a workshop"></div>
<div class="abs support-panel">
  <h3>COMPLETE PRIMARY AND SECONDARY<br>SCHOOL SUPPORT</h3>
  <p>We offer support in all aspects of ICT in education, from technical faults to assisting teachers and coordinators to meet the requirements of the computing curriculum</p>
</div>
<div class="btn" style="top:1671px;left:499px;width:197px;height:46px">Find out more</div>

<!-- What we do -->
<h2 class="h2 center" style="top:1860px;font-size:38px">WHAT WE DO</h2>
<p class="abs center" style="top:1940px;font-size:17px;line-height:35px;color:#555">We provide a range of services, each service will be tailored to<br>meet the individual needs of each school</p>

<div class="card" style="left:114px">
  <div class="card-icon" role="img" aria-label="Icon of a support technician with gear"></div>
  <h4>ICT Support</h4>
  <p>Orvan Logic provides managed support contracts taccommodate the individual needs of a school, as we understand that every.</p>
</div>
<div class="card" style="left:457px">
  <div class="card-icon" role="img" aria-label="Icon of computer hardware"></div>
  <h4>Hardware Sales</h4>
  <p>We supply and install hardware from the world's leading manufacturersincluding: Norvik, Castellan.</p>
</div>
<div class="card" style="left:793px">
  <div class="card-icon" role="img" aria-label="Icon of a cloud hosting web page"></div>
  <h4>Cloud &amp; Hosting<br>Services</h4>
  <p>We offer an extensive range of cloud and hosting services includingwebsites,domains,blogs emails and cloud storage.</p>
</div>
<div class="btn" style="top:2382px;left:179px;width:155px;height:45px">Read more</div>
<div class="btn" style="top:2382px;left:522px;width:155px;height:45px">Read more</div>
<div class="btn" style="top:2382px;left:858px;width:155px;height:45px">Read more</div>

<!-- Testimonials -->
<div class="abs testi"></div>
<h2 class="h2 center" style="top:2590px;font-size:36px;color:var(--white)">TESTIMONIALS</h2>
<div class="quote-mark" style="top:2650px;left:118px">&ldquo;</div>
<div class="abs testi-quote">"The team at Orvan Logic offer a fantastic service. They are reliable and approachable and ensure the smooth running of our school network. Their technical knowledge is excellent and love the challenge of solving new problems! Nothing is too much for Tom as he understands how schools operate.</div>
<div class="quote-mark" style="top:2775px;left:1002px">&rdquo;</div>
<div class="abs center testi-author">- Megan Holloway, Computing Coordinator at Ashgrove Lane Primary School</div>
<span class="dot" style="top:2907px;left:570px"></span>
<span class="dot" style="top:2907px;left:594px"></span>
<span class="dot" style="top:2907px;left:618px"></span>

<!-- Partners -->
<h2 class="h2 center" style="top:3065px;font-size:38px">OUR PARTNERS</h2>
<div class="partner" style="left:103px"><span></span></div>
<div class="partner" style="left:305px"><span></span></div>
<div class="partner" style="left:502px"><span></span></div>
<div class="partner" style="left:705px"><span></span></div>
<div class="partner" style="left:911px"><span></span></div>
<span class="dot" style="top:3194px;left:1127px;width:10px;height:10px;background:var(--blue)"></span>
<span class="dot" style="top:3212px;left:1127px;width:10px;height:10px;background:var(--blue)"></span>
<span class="dot" style="top:3230px;left:1127px;width:10px;height:10px;background:var(--blue)"></span>

<!-- Stats -->
<div class="abs stats" role="img" aria-label="Blue-tinted photo of server racks"></div>
<div class="stat" style="left:190px"><b>40,2560</b><i>Clients</i></div>
<div class="stat" style="left:406px"><b>120</b><i>Country</i></div>
<div class="stat" style="left:623px"><b>56,564</b><i>Business</i></div>
<div class="stat" style="left:840px"><b>45,645</b><i>People</i></div>

<!-- Contact -->
<h2 class="h2" style="top:3820px;left:108px;font-size:33px">CONTACT US</h2>
<h2 class="h2" style="top:3820px;left:688px;font-size:33px">GET IN TOUCH</h2>
<svg class="abs" style="top:3928px;left:136px" width="18" height="26" viewBox="0 0 18 26"><path d="M9 0a9 9 0 00-9 9c0 7 9 17 9 17s9-10 9-17a9 9 0 00-9-9z" fill="var(--blue)"/><circle cx="9" cy="9" r="3.5" fill="#fff"/></svg>
<div class="info" style="top:3923px">Harbour House, Linden<br>Street Bury,Lancashire,<br>BL0 9ZZ</div>
<svg class="abs" style="top:4045px;left:134px" width="22" height="22" viewBox="0 0 24 24"><path d="M6.6 10.8a15 15 0 006.6 6.6l2.2-2.2a1 1 0 011-.25 11.4 11.4 0 003.6.57 1 1 0 011 1V20a1 1 0 01-1 1A17 17 0 013 4a1 1 0 011-1h3.5a1 1 0 011 1 11.4 11.4 0 00.57 3.6 1 1 0 01-.25 1z" fill="var(--blue)"/></svg>
<div class="info" style="top:4040px">0161 555 0192</div>
<svg class="abs" style="top:4108px;left:133px" width="24" height="17" viewBox="0 0 22 16"><rect x="1" y="1" width="20" height="14" rx="1" fill="none" stroke="var(--blue)" stroke-width="2"/><path d="M1 2l10 7 10-7" fill="none" stroke="var(--blue)" stroke-width="2"/></svg>
<div class="info" style="top:4098px">info@orvan-logic.co.uk</div>

<div class="field" style="top:3914px;left:560px;width:235px;height:50px">First Name</div>
<div class="field" style="top:3914px;left:828px;width:236px;height:50px">Last Name</div>
<div class="field" style="top:3984px;left:560px;width:235px;height:49px">Phone</div>
<div class="field" style="top:3984px;left:828px;width:236px;height:49px">Email</div>
<div class="field" style="top:4058px;left:560px;width:504px;height:103px">Message</div>
<div class="btn" style="top:4214px;left:754px;width:155px;height:43px">Read more</div>

<div class="abs live-chat">
  <svg width="30" height="26" viewBox="0 0 30 26"><rect x="1" y="1" width="20" height="14" rx="3" fill="none" stroke="#fff" stroke-width="2"/><path d="M9 19h13l5 5v-5h1V8" fill="none" stroke="#fff" stroke-width="2"/></svg>
  Live Chat
</div>

<!-- Footer -->
<div class="abs footer"></div>
<div class="abs brand foot-brand"><span class="brand-square"></span>Orvan Logic</div>
<div class="abs center foot-nav"><span>HOME</span><span>SERVICES</span><span>ABOUT US</span><span>HELP &nbsp;DESK</span><span>CONTACT</span></div>
<span class="social" style="left:533px"></span>
<span class="social" style="left:580px"></span>
<span class="social" style="left:631px"></span>
<div class="abs center copyright">Copyrights 2020. All rights reserved</div>

</body>
</html>
```